Golf Course hole signage

I would like to have a golf course sign created for our wealth management business. I would like to incorporate the logo branding and have my full name and role in the signage. I would also like to apply our services in the signage if possible or if size permits. We do Investment planning, financial planning, retirement planning, Tax planning and insurance planning.

My current role at the business is the following:

Marcus Dell, CIM®, CIWM®
Associate Wealth Manager

Email: Marcus.dell@Rvtcap.ca

Cell: 204-618-4039

Company: RV Tandem Capital

The division of the company: RV Holdings Inc.

I have also attached a photo of an older sign to give you a better idea of what the rough size would need to be!

Target Market(s)

High networth individual

Industry/Entity Type

Wealth Management

Colors
0054AA
0677BA
7BADD7
CADEEF
E8F1F8

Requirements
Nice to have
• Modern type style

```html
<!DOCTYPE html>
<html lang="en">
<head>
<meta charset="utf-8">
<title>Golf Hole Signage – Marcus Dell</title>
<link rel="stylesheet" href="https://fonts.googleapis.com/css2?family=Roboto+Condensed:wght@300;800;900&family=Arimo:wght@400;700&display=swap">
<style>
  :root {
    --navy: #062a5c;
    --paper: #ffffff;
    --mark: #0054aa;
  }
  html, body {
    margin: 0;
    padding: 0;
    width: 1200px;
    height: 1200px;
    overflow: hidden;
    background: var(--paper);
  }
  .canvas {
    position: relative;
    width: 1200px;
    height: 1200px;
    background: var(--paper);
    color: var(--navy);
    overflow: hidden;
  }
  .headline,
  .subline {
    position: absolute;
    margin: 0;
    transform: translateX(-50%);
    white-space: nowrap;
    text-transform: uppercase;
    font-family: "Roboto Condensed", "Arial Narrow", sans-serif;
    line-height: 1;
  }
  .sign-putt .headline {
    left: 620px;
    top: 88px;
    font-size: 318px;
    font-weight: 900;
    letter-spacing: -4px;
  }
  .sign-putt .subline {
    left: 620px;
    top: 362px;
    font-size: 70px;
    font-weight: 800;
    letter-spacing: 0;
  }
  .sign-sand .headline {
    left: 604px;
    top: 768px;
    font-size: 166px;
    font-weight: 900;
    letter-spacing: 1px;
  }
  .sign-sand .subline {
    left: 604px;
    top: 925px;
    font-size: 50px;
    font-weight: 300;
  }
  .contact-row {
    position: absolute;
    left: 0;
    width: 1200px;
    height: 60px;
    font-family: "Arimo", Arial, sans-serif;
  }
  .sign-putt .contact-row { top: 506px; }
  .sign-sand .contact-row { top: 1110px; }
  .advisor {
    position: absolute;
    left: 66px;
    width: 396px;
    text-align: center;
    line-height: 1.05;
  }
  .advisor-name {
    display: block;
    font-size: 23px;
    font-weight: 700;
  }
  .advisor-role {
    display: block;
    font-size: 22px;
    font-weight: 400;
  }
  .reach {
    position: absolute;
    left: 697px;
    transform: translateX(-50%);
    top: -4px;
    text-align: center;
    font-size: 24px;
    font-weight: 400;
    line-height: 1.08;
    white-space: nowrap;
  }
  .firm {
    position: absolute;
    left: 933px;
    top: 4px;
    display: flex;
    align-items: center;
    gap: 8px;
  }
  .firm-square {
    width: 36px;
    height: 36px;
    background: var(--mark);
  }
  .firm-name {
    font-size: 16px;
    font-weight: 700;
    text-transform: uppercase;
    line-height: 1.1;
    color: var(--navy);
  }
</style>
</head>
<body>
<main class="canvas">

  <section class="sign sign-putt">
    <h1 class="headline">Putt</h1>
    <p class="subline">Your money to work</p>
    <div class="contact-row">
      <div class="advisor">
        <span class="advisor-name">Marcus Dell, CIM®, CIWM®</span>
        <span class="advisor-role">Associate Wealth Manager</span>
      </div>
      <div class="reach">
        <div class="reach-email">Marcus.dell@Rvtcap.ca</div>
        <div class="reach-phone">204-618-4039</div>
      </div>
      <div class="firm">
        <span class="firm-square"></span>
        <span class="firm-name">RV Tandem<br>Capital</span>
      </div>
    </div>
  </section>

  <section class="sign sign-sand">
    <h2 class="headline">No sand traps</h2>
    <p class="subline">In my financial strategies</p>
    <div class="contact-row">
      <div class="advisor">
        <span class="advisor-name">Marcus Dell, CIM®, CIWM®</span>
        <span class="advisor-role">Associate Wealth Manager</span>
      </div>
      <div class="reach">
        <div class="reach-email">Marcus.dell@Rvtcap.ca</div>
        <div class="reach-phone">204-618-4039</div>
      </div>
      <div class="firm">
        <span class="firm-square"></span>
        <span class="firm-name">RV Tandem<br>Capital</span>
      </div>
    </div>
  </section>

</main>
</body>
</html>
```